Apartments rental business needs a web for direct reservations.

I need a website that allows my clients to check the property (pictures, a brief description etc) and lets them make reservations. They will be providing the required information such as name, last name, email address and credit card details. Also a calendar where I can update the availability (dates and prices) of the property upon new reservations is a must. I already have a logo that should also be a good starting point for colors, style an inspiration.

Need extra days to review

```html
<!DOCTYPE html>
<html lang="en">
<head>
<meta charset="utf-8">
<title>Alderton Apartments – Direct Reservations</title>
<link rel="stylesheet" href="https://fonts.googleapis.com/css2?family=Tinos:wght@400;700&family=Arimo:wght@400;700&display=swap">
<style>
  :root{
    --purple:#8e1a86;
    --cream:#ffffe0;
    --white:#ffffff;
    --yellow:#f4f433;
    --red:#f01010;
    --blue:#1d8ff2;
    --line-blue:#1c2fa6;
    --sky:#5d86b5;
    --tree:#22402f;
    --house:#e6e4dc;
    --ink:#102060;
    --gold:#b9852b;
    --free:#d9f7d0;
    --booked:#f4b3b3;
  }
  *{box-sizing:border-box;margin:0;padding:0}
  html,body{width:1200px;height:694px;overflow:hidden;background:var(--white)}
  .site{width:1200px;height:694px;background:var(--cream);font-family:"Tinos",serif;overflow:hidden}

  .topbar{height:44px;background:var(--purple);display:flex;align-items:center;padding:0 12px;gap:6px}
  .nav-link{height:32px;padding:0 28px;border:1px solid #c78cc3;color:var(--white);font-size:13px;display:flex;align-items:center;letter-spacing:.5px;white-space:nowrap}
  .nav-spacer{width:14px}
  .login-field{height:24px;width:122px;background:var(--white);border:1px solid #999;font-size:11px;color:#666;display:flex;align-items:center;justify-content:center;margin-left:8px}
  .login-btn{height:24px;width:58px;background:var(--yellow);font-size:11px;display:flex;align-items:center;justify-content:center;margin-left:8px;color:#333}

  .hero{height:264px;background:linear-gradient(180deg,var(--sky) 0%,#8fb0d2 22%,var(--tree) 45%,#5b6650 60%,var(--house) 72%,#c9c3b2 100%)}

  .unit-type{height:20px;background:var(--purple);display:flex;align-items:center;gap:270px;padding-left:12px;color:var(--white);font-size:10px}
  .unit-type span{display:flex;align-items:center;gap:5px;white-space:nowrap}
  .unit-type i{width:9px;height:9px;border-radius:50%;background:var(--white);display:inline-block}
  .unit-type i.on{box-shadow:inset 0 0 0 2px var(--white);background:var(--gold)}

  .reserve{height:40px;background:var(--purple);display:flex;align-items:center;padding:0 6px;gap:8px}
  .field{height:28px;flex:1;min-width:0;background:var(--white);border:1px solid #aaa;font-size:12px;color:#666;display:flex;align-items:center;justify-content:center;white-space:nowrap}
  .field.select{justify-content:space-between;padding:0 8px;color:var(--gold);font-weight:700}
  .reserve-btn{height:28px;width:130px;flex:none;background:var(--red);color:var(--white);font-size:12px;display:flex;align-items:center;justify-content:center;margin-left:20px}

  .divider{height:3px;background:var(--line-blue);margin:12px 12px 0}

  .listings{display:flex;gap:24px;padding:22px 0 0 40px}
  .card{width:524px}
  .card-photo{height:218px}
  .card-photo.one{background:linear-gradient(180deg,#d8e2ec 0%,#b9b7ae 50%,#676862 100%)}
  .card-photo.two{background:linear-gradient(180deg,#b9b09c 0%,#b48a55 45%,#4e5a3a 100%)}
  .card-info{height:62px;background:var(--blue);font-family:"Arimo",sans-serif;font-size:11px;color:var(--ink);padding:4px 8px}
  .card-info .row{display:flex;justify-content:space-between;white-space:nowrap}
  .calendar{display:flex;gap:4px;margin-top:4px}
  .day{flex:1;height:34px;background:var(--free);font-size:9px;line-height:11px;text-align:center;padding-top:2px;color:var(--ink)}
  .day b{display:block;font-size:10px}
  .day.booked{background:var(--booked);color:#7a1010}
</style>
</head>
<body>
<div class="site">
  <header class="topbar">
    <span class="nav-link">HOME</span>
    <span class="nav-link">CONTACT US</span>
    <span class="nav-link">ABOUT US</span>
    <span class="nav-link">NOTIFICATION</span>
    <span class="nav-spacer"></span>
    <span class="login-field">Enter Email</span>
    <span class="login-field">Enter Password</span>
    <span class="login-btn">Sign</span>
  </header>

  <div class="hero" role="img" aria-label="Photo of a large white apartment house among pine trees under a cloudy sky"></div>

  <div class="unit-type">
    <span><i class="on"></i>Studio</span>
    <span><i></i>One Bedroom</span>
    <span><i></i>Two Bedroom</span>
  </div>

  <form class="reserve">
    <span class="field select">ALDERTON <span>&#9662;</span></span>
    <span class="field">First Name</span>
    <span class="field">Last Name</span>
    <span class="field">Email Address</span>
    <span class="field">Card Number</span>
    <span class="field">Check-in 12/06</span>
    <span class="field">Check-out 15/06</span>
    <span class="reserve-btn">Reserve</span>
  </form>

  <div class="divider"></div>

  <main class="listings">
    <article class="card">
      <div class="card-photo one" role="img" aria-label="Photo of a white two-storey apartment building with a gated front"></div>
      <div class="card-info">
        <div class="row"><span>Garden Studio</span><span>2 Guests</span><span>Free Wi-Fi</span><span>From $90 / night</span></div>
        <div class="calendar">
          <div class="day"><b>12</b>Mon $90</div>
          <div class="day"><b>13</b>Tue $90</div>
          <div class="day booked"><b>14</b>Booked</div>
          <div class="day booked"><b>15</b>Booked</div>
          <div class="day"><b>16</b>Fri $110</div>
          <div class="day"><b>17</b>Sat $120</div>
          <div class="day"><b>18</b>Sun $110</div>
        </div>
      </div>
    </article>
    <article class="card">
      <div class="card-photo two" role="img" aria-label="Photo of a modern beige apartment house with a front lawn"></div>
      <div class="card-info">
        <div class="row"><span>Terrace Suite</span><span>4 Guests</span><span>Parking</span><span>From $140 / night</span></div>
        <div class="calendar">
          <div class="day"><b>12</b>Mon $140</div>
          <div class="day booked"><b>13</b>Booked</div>
          <div class="day"><b>14</b>Wed $140</div>
          <div class="day"><b>15</b>Thu $140</div>
          <div class="day booked"><b>16</b>Booked</div>
          <div class="day booked"><b>17</b>Booked</div>
          <div class="day"><b>18</b>Sun $160</div>
        </div>
      </div>
    </article>
  </main>
</div>
</body>
</html>
```